flyer for roofing advertising

Need a modern, bold, luxurious advertisement flyer for our roofing company. located in buffalo, ny. Big house with a intense roof design asphalt shingles. slogan is "Reliability starts at the top". Colors varies but want it to be modern. we will be handing these out when we are working in the area. phone number is 716-555-0147 for the NO K.W estimate. also our services are roofing, roof repairs, gutters, attic ventilation. we offer a 15 year warranty with our platinum roof program. We are certified by dwellmatch, harlan trevisk, quarno. Also follow us on linkpage, wexora and frunt. website is ktw-roofing.com, linkpage is ktwroofing. pictures are on linkpage and our website if need more can be provided. also can include a review we have.

```html
<!DOCTYPE html>
<html lang="en">
<head>
<meta charset="utf-8">
<title>KTW Roofing Flyer</title>
<link href="https://fonts.googleapis.com/css2?family=Montserrat:wght@600;700;800;900&family=Lato:wght@400;700&display=swap" rel="stylesheet">
<style>
  :root {
    --backdrop: #3e3b3a;
    --orange: #f4911e;
    --ink: #1f1f1f;
    --dark-bar: #2d2c2c;
    --paper: #ffffff;
    --tab: #2f2f2f;
    --body-text: #2a2a2a;
  }
  * { margin: 0; padding: 0; box-sizing: border-box; }
  html, body { width: 1200px; height: 1200px; overflow: hidden; background: var(--backdrop); }
  body { position: relative; font-family: "Lato", sans-serif; color: var(--body-text); }

  .flyer {
    position: absolute; left: 234px; top: 118px;
    width: 709px; height: 1004px;
    background: var(--paper);
    overflow: hidden;
  }
  .hero-art { position: absolute; left: 0; top: 0; width: 709px; height: 500px; }

  .logo-tab {
    position: absolute; left: 558px; top: 0; width: 120px; height: 98px;
    display: flex; flex-direction: column; align-items: center; justify-content: center;
    padding-bottom: 14px;
  }
  .logo-tab svg { position: absolute; inset: 0; }
  .logo-name {
    position: relative; font-family: "Montserrat", sans-serif; font-weight: 800;
    font-size: 20px; color: var(--orange); display: flex; align-items: center; gap: 5px;
  }
  .logo-name .mark { width: 9px; height: 9px; background: var(--orange); }
  .logo-tagline {
    position: relative; font-family: "Montserrat", sans-serif; font-weight: 600;
    font-size: 6px; color: var(--orange); letter-spacing: 0.3px; margin-top: 4px;
  }

  .headline {
    position: absolute; left: 0; top: 440px; width: 709px; text-align: center;
    font-family: "Montserrat", sans-serif; font-weight: 900; line-height: 1;
  }
  .headline .lead { display: block; color: var(--orange); font-size: 58px; letter-spacing: 0.5px; }
  .headline .rest { display: block; color: var(--ink); font-size: 50px; margin-top: 4px; letter-spacing: 1px; }

  .work-photo {
    position: absolute; left: 59px; width: 155px;
    border: 5px solid var(--orange);
  }
  .work-photo.install { top: 563px; height: 119px; background: linear-gradient(160deg, #d9dde2 0%, #b9a58c 55%, #6e5440 100%); }
  .work-photo.siding { top: 694px; height: 118px; background: linear-gradient(150deg, #6d6460 0%, #d8b6b3 50%, #e9d0cf 100%); }
  .work-photo.repair { top: 828px; height: 114px; background: linear-gradient(135deg, #7b7570 0%, #5b5550 60%, #6f8a4b 100%); }

  .side-tab {
    position: absolute; left: 34px; width: 24px;
    background: var(--tab); color: #fff;
    font-size: 12px; writing-mode: vertical-rl; transform: rotate(180deg);
    display: flex; align-items: center; justify-content: center;
  }
  .side-tab.install { top: 566px; height: 114px; }
  .side-tab.siding { top: 708px; height: 92px; }
  .side-tab.repair { top: 846px; height: 80px; }

  .content { position: absolute; left: 239px; top: 0; width: 430px; }
  .section-title {
    position: absolute; left: 0; font-family: "Montserrat", sans-serif; font-weight: 700;
    font-size: 20px; color: var(--ink); display: flex; align-items: center; gap: 10px;
    white-space: nowrap;
  }
  .section-title::after { content: ""; display: block; height: 1.5px; background: var(--ink); width: 118px; }
  .section-title.about { top: 561px; }
  .section-title.services { top: 702px; }

  .copy { position: absolute; left: 0; width: 425px; font-size: 10.6px; line-height: 14.4px; }
  .copy.about-1 { top: 591px; }
  .copy.about-2 { top: 663px; }
  .copy.call-body { top: 867px; width: 440px; font-size: 10.4px; }

  .service {
    position: absolute; display: flex; align-items: center; gap: 5px;
    font-size: 12.6px; white-space: nowrap; color: var(--ink);
  }
  .service svg { width: 19px; height: 19px; flex: none; }

  .call-title {
    position: absolute; left: 2px; top: 827px; font-family: "Montserrat", sans-serif;
    font-weight: 700; font-size: 13px; line-height: 17.5px; color: var(--ink); letter-spacing: 0.6px;
  }
  .call-title .rule { display: inline-block; width: 118px; height: 1.5px; background: var(--ink); vertical-align: middle; margin-left: 8px; }

  .footer-bar {
    position: absolute; left: 0; top: 952px; width: 709px; height: 52px;
    background: var(--dark-bar); color: #fff;
    font-family: "Montserrat", sans-serif; font-weight: 700; font-size: 13px;
  }
  .footer-item { position: absolute; display: flex; align-items: center; gap: 10px; }
  .footer-item svg { width: 20px; height: 20px; flex: none; }
  .footer-item.phone { left: 26px; top: 16px; }
  .footer-item.web { left: 230px; top: 14px; }
  .footer-item.address { right: 28px; top: 8px; text-align: right; line-height: 16px; }
</style>
</head>
<body>
<main class="flyer">
  <svg class="hero-art" viewBox="0 0 709 500" aria-hidden="false">
    <defs>
      <linearGradient id="houseTones" x1="0" y1="0" x2="0" y2="1">
        <stop offset="0" stop-color="#4c5868"/>
        <stop offset="0.35" stop-color="#3b4048"/>
        <stop offset="0.6" stop-color="#b59d82"/>
        <stop offset="0.85" stop-color="#d9d6d2"/>
        <stop offset="1" stop-color="#8a7a68"/>
      </linearGradient>
    </defs>
    <rect x="0" y="0" width="709" height="450" fill="url(#houseTones)" role="img" aria-label="Photo of a two-storey suburban house with a dark asphalt shingle roof, tan siding, brick front and white double garage door"/>
    <polygon points="0,434 355,358 709,434 709,500 0,500" fill="#ffffff"/>
    <polygon points="0,446 355,378 709,446 709,482 355,406 0,482" fill="#f4911e"/>
  </svg>

  <div class="logo-tab">
    <svg viewBox="0 0 120 98" aria-hidden="true"><polygon points="0,0 120,0 120,98 60,82 0,98" fill="#ffffff"/></svg>
    <div class="logo-name"><span class="mark"></span>KTW</div>
    <div class="logo-tagline">ROOFING-SIDING-STONE</div>
  </div>

  <h1 class="headline"><span class="lead">RELIABILITY</span><span class="rest">STARTS AT THE TOP</span></h1>

  <div class="side-tab install">Roof Installation</div>
  <div class="work-photo install" role="img" aria-label="Roofer installing new roof decking on a snowy day"></div>
  <div class="side-tab siding">Siding Repair</div>
  <div class="work-photo siding" role="img" aria-label="House wrap and foam board laid out for siding repair"></div>
  <div class="side-tab repair">Roof Repair</div>
  <div class="work-photo repair" role="img" aria-label="Roofer repairing shingles seen from above"></div>

  <section class="content">
    <h2 class="section-title about">About Us</h2>
    <p class="copy about-1">KTW Roofing got its start in 1996. Today, we remain family-owned and -operated by three professionals who have 40 years of combined experience. We're not only the preferred roofing company for installation, repair, and other services, but we've also worked hard to earn the title of Harlan Trevisk Preferred Contractor.</p>
    <p class="copy about-2">KTW Roofing works with safety and longevity in mind: the safety of you and everyone inside your home or commercial property, and the longevity of your roof.</p>

    <h2 class="section-title services">Services</h2>
    <div class="service" style="left:0;top:740px"><svg viewBox="0 0 20 20"><circle cx="10" cy="10" r="9" fill="#f4911e" stroke="#2d2c2c" stroke-width="1"/><path d="M4 12 L10 7 L16 12" fill="none" stroke="#2d2c2c" stroke-width="1.6"/></svg>Roof Installation</div>
    <div class="service" style="left:173px;top:740px"><svg viewBox="0 0 20 20"><circle cx="10" cy="10" r="9" fill="#f4911e" stroke="#2d2c2c" stroke-width="1"/><path d="M5 13 L10 8 L15 13 Z" fill="#2d2c2c"/></svg>Roof Repair</div>
    <div class="service" style="left:325px;top:740px"><svg viewBox="0 0 20 20"><circle cx="10" cy="10" r="9" fill="#f4911e" stroke="#2d2c2c" stroke-width="1"/><rect x="5" y="7" width="10" height="6" rx="2" fill="none" stroke="#2d2c2c" stroke-width="1.6"/></svg>Re-roof</div>
    <div class="service" style="left:0;top:768px"><svg viewBox="0 0 20 20"><circle cx="10" cy="10" r="9" fill="#f4911e" stroke="#2d2c2c" stroke-width="1"/><rect x="6" y="7" width="8" height="7" fill="none" stroke="#2d2c2c" stroke-width="1.5"/></svg>Commercial Roofing</div>
    <div class="service" style="left:173px;top:768px"><svg viewBox="0 0 20 20"><circle cx="10" cy="10" r="9" fill="#f4911e" stroke="#2d2c2c" stroke-width="1"/><circle cx="9" cy="9" r="3" fill="none" stroke="#2d2c2c" stroke-width="1.5"/><path d="M11 11 L14 14" stroke="#2d2c2c" stroke-width="1.6"/></svg>Roof Inspection</div>
    <div class="service" style="left:325px;top:768px"><svg viewBox="0 0 20 20"><circle cx="10" cy="10" r="9" fill="#f4911e" stroke="#2d2c2c" stroke-width="1"/><path d="M6 14 L12 8" stroke="#2d2c2c" stroke-width="2.2"/><circle cx="13" cy="7" r="2.2" fill="none" stroke="#2d2c2c" stroke-width="1.5"/></svg>Siding Repair</div>
    <div class="service" style="left:0;top:797px"><svg viewBox="0 0 20 20"><circle cx="10" cy="10" r="9" fill="#f4911e" stroke="#2d2c2c" stroke-width="1"/><path d="M6 6 H14 M7 9 H13 M8 12 H12" stroke="#2d2c2c" stroke-width="1.5"/></svg>New Siding Installation</div>
    <div class="service" style="left:173px;top:797px"><svg viewBox="0 0 20 20"><circle cx="10" cy="10" r="9" fill="#f4911e" stroke="#2d2c2c" stroke-width="1"/><path d="M6 6 V14 H14 M9 6 V11" fill="none" stroke="#2d2c2c" stroke-width="1.5"/></svg>Gutters</div>

    <h2 class="call-title">CALL THE BEST ROOFING CONTRACTOR IN<br>WESTERN NEW YORK<span class="rule"></span></h2>
    <p class="copy call-body">Roofing contractors certainly aren't few and far between in Niagara County and Erie County, but the best ones shouldn't be hard to find. If you live in Pendleton, NY; Amherst, NY; Orchard Park, NY; or Clarence, NY, you won't have to look hard for a reliable roofing company. KTW Roofing is the go-to business for roof installation, roof repair, re-roofing, commercial roofing, roof inspections, gutter, and siding jobs of all scopes and sizes.</p>
  </section>

  <footer class="footer-bar">
    <div class="footer-item phone">
      <svg viewBox="0 0 24 24"><path d="M6 3 L9 3 L10.5 7.5 L8.5 9 C9.5 11.5 12.5 14.5 15 15.5 L16.5 13.5 L21 15 L21 18 C21 19.5 19.5 21 18 21 C10 20.5 3.5 14 3 6 C3 4.5 4.5 3 6 3 Z" fill="none" stroke="#fff" stroke-width="1.6"/></svg>
      <span>716-555-0147</span>
    </div>
    <div class="footer-item web">
      <svg viewBox="0 0 24 24"><circle cx="12" cy="12" r="9.5" fill="none" stroke="#fff" stroke-width="1.8"/><path d="M2.5 12 H21.5 M12 2.5 C8 7 8 17 12 21.5 M12 2.5 C16 7 16 17 12 21.5" fill="none" stroke="#fff" stroke-width="1.4"/></svg>
      <span>www.ktw-roofing.com</span>
    </div>
    <div class="footer-item address">
      <span>4127 Marlow Rd, Lockport,<br>NY 14094</span>
      <svg viewBox="0 0 24 24" style="width:24px;height:30px"><path d="M12 2 C7.5 2 5 5.5 5 9 C5 14 12 20 12 20 C12 20 19 14 19 9 C19 5.5 16.5 2 12 2 Z" fill="none" stroke="#fff" stroke-width="1.8"/><circle cx="12" cy="9" r="2.6" fill="none" stroke="#fff" stroke-width="1.6"/><ellipse cx="12" cy="21.5" rx="6" ry="1.6" fill="none" stroke="#fff" stroke-width="1.4"/></svg>
    </div>
  </footer>
</main>
</body>
</html>
```